Counselling practice needs a Business Card Design

I need a business card design for a new counselling practice in Canberra, Australia. The name of the practice is Dr Henry Walsh, Counselling Services and the practice focuses on philosophical, narrative and existential counselling for individuals, couples and families. The final design should communicate professionalism, sophistication of analysis and psychological wholeness. The reverse side of the card should have an appointment reminder
Updates

Could the following qualifications also be included on card. BSc (Psychology), BA hons (Philosophy), PhD (Philosophy), Diploma of Community Counselling And the following affiliation Guild of Talk Therapists of Tasvale and District Inc. (GOTTTD) And my contact phone mobile phone number is 0455837190, and email is Henry.Walsh937@mailbrook.example for inclusion as well.

Thank you all who have put in a design so far. I just wanted to clarify some design points based on what you have submitted. 1. The Guild of Talk Therapists. Tasvale and District Inc. (GOTTTD) is an affiliation only. 'Member of the Guild of Talk Therapists. Tasvale and District Inc (GOTTTD)' should appear with the same prominence of a qualification. 2. The Post Graduate Diploma in Community Counselling is a quaification and should appear as 'PG Dip (Community Counselling)' after the other qualifications. 3. I am advertising myself as a counsellor so 'Dr Henry Walsh, Counselling Services' or 'Dr Henry Walsh, Counsellor' is the equivalent of the business name. After looking at some of the designs I prefer Dr Henry Walsh in sentence case rather than all capitals (DR HENRY WALSH). 4. 'Philosophical, narrative and existential counselling for individuals, couples and families' is the description of the type of counselling services and should appear on the card.

One further point. I have updated my email address for the card. It is now drhenrywalsh@tasvaletherapy.example

```html
<!DOCTYPE html>
<html lang="en">
<head>
<meta charset="utf-8">
<title>Dr Henry Walsh – Counselling Services Business Card</title>
<link rel="stylesheet" href="https://fonts.googleapis.com/css2?family=Tinos&family=Open+Sans:wght@400;600&display=swap">
<style>
  :root {
    --backdrop: #9a9795;
    --card: #ffffff;
    --brand-blue: #2f5fae;
    --ink-grey: #4a4a4a;
    --rule-dots: #8a8a8a;
    --faint-mark: #ececec;
    --serif: "Tinos", "Times New Roman", serif;
    --sans: "Open Sans", Arial, sans-serif;
  }
  * { box-sizing: border-box; margin: 0; padding: 0; }
  html, body {
    width: 1200px; height: 900px; overflow: hidden;
    background: var(--backdrop);
  }
  .stage {
    width: 1200px; height: 900px;
    display: flex; align-items: center; justify-content: center; gap: 60px;
  }
  .card {
    position: relative;
    width: 520px; height: 310px;
    background: var(--card);
    border-radius: 22px;
    overflow: hidden;
    box-shadow: 0 10px 24px rgba(0,0,0,0.18);
  }

  /* Front */
  .brand-mark {
    position: absolute; left: 50%; top: 18px;
    width: 72px; height: 72px; margin-left: -36px;
    border-radius: 50%;
    border: 7px solid var(--brand-blue);
  }
  .brand-name {
    position: absolute; left: 0; right: 0; top: 96px;
    text-align: center;
    font-family: var(--serif); font-size: 42px; font-weight: 400;
    color: var(--brand-blue); line-height: 1;
  }
  .brand-tagline {
    position: absolute; left: 0; right: 0; top: 142px;
    text-align: center;
    font-family: var(--serif); font-size: 11px; letter-spacing: 6px;
    color: var(--brand-blue);
  }
  .brand-rule {
    position: absolute; left: 0; right: 0; top: 160px;
    height: 5px; background: var(--brand-blue);
  }
  .credentials {
    position: absolute; left: 0; right: 0; top: 176px;
    text-align: center;
    font-family: var(--sans); font-size: 9px; line-height: 1.35;
    color: var(--brand-blue);
  }
  .contact {
    position: absolute; left: 0; right: 0; top: 236px;
    text-align: center; font-family: var(--sans); color: var(--ink-grey);
  }
  .contact .phone { font-size: 20px; line-height: 1.2; }
  .contact .email { font-size: 14px; }

  /* Back */
  .faint-ring {
    position: absolute; left: 250px; top: 20px;
    width: 280px; height: 280px;
    border-radius: 50%;
    border: 22px solid var(--faint-mark);
  }
  .appointments-title {
    position: absolute; left: 0; right: 0; top: 58px;
    text-align: center;
    font-family: var(--sans); font-size: 16px;
    color: var(--brand-blue); text-decoration: underline;
  }
  .field {
    position: absolute; display: flex; align-items: baseline;
    font-family: var(--sans); font-size: 15px; font-weight: 600;
    color: var(--ink-grey);
  }
  .field .line {
    flex: 1; margin-left: 6px;
    border-bottom: 1px dotted var(--rule-dots);
    transform: translateY(-3px);
  }
  .field-name { left: 30px; right: 26px; top: 102px; }
  .field-date { left: 30px; width: 210px; top: 144px; }
  .field-time { left: 280px; right: 26px; top: 138px; font-size: 13px; }
  .back-signature {
    position: absolute; right: 26px; bottom: 46px;
    display: flex; align-items: center; gap: 6px;
  }
  .back-signature .dot {
    width: 32px; height: 32px; border-radius: 50%;
    border: 4px solid var(--brand-blue);
  }
  .back-signature .words { font-family: var(--serif); color: var(--brand-blue); line-height: 1; }
  .back-signature .name { font-size: 20px; }
  .back-signature .tag { font-size: 5px; letter-spacing: 2.4px; margin-top: 2px; }
</style>
</head>
<body>
<main class="stage">
  <section class="card card-front">
    <div class="brand-mark"></div>
    <h1 class="brand-name">Dr Henry Walsh</h1>
    <p class="brand-tagline">COUNSELLING SERVICES</p>
    <div class="brand-rule"></div>
    <p class="credentials">
      BSc (Psychology), BA hons (Philosophy), PhD (Philosophy),<br>
      Diploma of Community Counselling<br>
      Guild of Talk Therapists of Tasvale and District Inc. (GOTTTD)
    </p>
    <div class="contact">
      <p class="phone">0455837190</p>
      <p class="email">drhenrywalsh@tasvaletherapy.example</p>
    </div>
  </section>

  <section class="card card-back">
    <div class="faint-ring"></div>
    <h2 class="appointments-title">Appointments</h2>
    <div class="field field-name">Name :<span class="line"></span></div>
    <div class="field field-date">Date :<span class="line"></span></div>
    <div class="field field-time">Time :<span class="line"></span></div>
    <div class="back-signature">
      <div class="dot"></div>
      <div class="words">
        <div class="name">Dr Henry Walsh</div>
        <div class="tag">COUNSELLING SERVICES</div>
      </div>
    </div>
  </section>
</main>
</body>
</html>
```